"Principles for action" poster design for inside company

I would like to create a poster in order to make a message from CEO to employees to be clearly.
A size is A3E(landscape) , and I wish you to design 3 messages(principles for action) into one poster.
("Principles for action" is core value for employees to do everything on working in our company.)
I want you to design and place 3 messages as if they have some relations each other in one poster.
Principles for actions are as follows;
(1)Bird's eye view:
(Meaning: Although there are multiple right answers, it is difficult to gain something if you do not have different view from common one. We request you always to compare subjective view and objective view and then aim to have the specific view.)
(2)Agility:
(Meaning: Maximum rapidity is obtained in any case. Rapid accumulation of trivial reply, delivery, and courtesy, and it will lead to overall competitiveness.)
(3)Back to comfort:
(Meaning:Whatever the type of business be, various ideas are generated by employees. Those born in uncomfortable environment, become bad product that are not comfortable. In other words, managers will be asked to keep the comfortable environment.)
(Summary)
Our company always require employees that "First, you grasp the meaning of everything as if having bird's eyes, and do action rapidly. if you do action rapidly, a lot of important things will be appeared, so that you grasp again on bird's eye.
In order to be these situation worked, it must be always required comfortable environment for employees, so that manager have to create and maintain comfortable environment.
-
No need to add the "meanings" of 3 message, but please place 3 message(Bird's eye view, Agility and Back to comfort) into a poster.
We like some desings below, but you don't need to be swayed too much by them. That is to say, we dont like messy design.
http://www.pixelbazaar.net/design/58203
http://www.pixelbazaar.net/design/49721
http://www.pixelbazaar.net/design/36094
http://www.pixelbazaar.net/design/2736519/poster-design-by-tovel
http://www.pixelbazaar.net/design/2736521/poster-design-by-tovel
http://www.pixelbazaar.net/design/2648092/poster-design-by-lumafoxxen
-
the attachment file is the logo data of our company. Please place it anywhere in the poster.

```html
<!DOCTYPE html>
<html lang="en">
<head>
<meta charset="utf-8">
<title>Principles of Action — Tandemly</title>
<link rel="stylesheet" href="https://fonts.googleapis.com/css2?family=Carlito:wght@400;700&family=Arimo:wght@400;700&display=swap">
<style>
  :root {
    --page: #ffffff;
    --paper: #e4dacb;
    --cloud-top: #74a6e6;
    --cloud-bottom: #2a5796;
    --orb: #4f80ba;
    --orb-edge: #1b2946;
    --night-cloud: #213f6c;
    --ink: #000000;
    --white: #ffffff;
    --red: #d2252b;
    --arrow-red: #b8463c;
    --arrow-mist: #c9d7ea;
    --teal: #2aa3c4;
    --gold: #f2c11b;
    --iris: #a86d45;
    --spiral: #a5141d;
    --brand-blue: #2f8fd0;
    --faint-blue: #9cc2e6;
  }
  html, body {
    margin: 0;
    padding: 0;
    width: 1200px;
    height: 728px;
    overflow: hidden;
    background: var(--page);
  }
  .poster {
    display: block;
    width: 1200px;
    height: 728px;
  }
  .poster text { font-family: "Carlito", "Arimo", sans-serif; }
  .title-text { font-family: "Arimo", sans-serif; font-weight: 700; fill: var(--red); font-size: 24px; }
  .brand-name { font-family: "Carlito", sans-serif; font-weight: 700; fill: var(--brand-blue); }
  .brand-faint { fill: var(--faint-blue); }
  .comfort-left { font-family: "Arimo", sans-serif; font-size: 58px; fill: var(--white); stroke: #222; stroke-width: 2; stroke-dasharray: 2 2; letter-spacing: 6px; }
  .comfort-right { font-family: "Arimo", sans-serif; font-size: 50px; fill: var(--white); stroke: #1c2a44; stroke-width: 1.5; letter-spacing: 4px; }
  .eye-word { fill: var(--white); font-size: 20px; }
  .eye-small { fill: #5d8ac4; font-size: 11px; letter-spacing: 4px; }
  .eye-caption { fill: var(--white); font-size: 10px; letter-spacing: 4px; }
  .agility-word { fill: #222; font-weight: 700; font-size: 24px; }
  .tag-text { fill: var(--red); font-family: "Arimo", sans-serif; font-weight: 700; font-size: 20px; }
  .discovery-text { fill: var(--white); font-size: 21px; stroke: #7a2a25; stroke-width: .6; }
  .complete-text { fill: var(--white); font-size: 15px; }
  .clarity-text { fill: #f06a6a; font-size: 20px; }
  .comfortable-text { font-family: "Arimo", sans-serif; font-weight: 700; font-size: 28px; letter-spacing: 11px; fill: #31528c; stroke: #6f95cf; stroke-width: .8; }
  .back-text { fill: var(--white); font-family: "Arimo", sans-serif; font-weight: 700; font-size: 18px; letter-spacing: 3px; }
</style>
</head>
<body>
<svg class="poster" viewBox="0 0 1140 690" preserveAspectRatio="none" xmlns="http://www.w3.org/2000/svg">
  <defs>
    <linearGradient id="cloud-fill" x1="0" y1="40" x2="0" y2="590" gradientUnits="userSpaceOnUse">
      <stop offset="0" stop-color="var(--cloud-top)"/>
      <stop offset="1" stop-color="var(--cloud-bottom)"/>
    </linearGradient>
    <linearGradient id="eye-area-fill" x1="0" y1="0" x2="0" y2="1">
      <stop offset="0" stop-color="#d9a21e"/>
      <stop offset="0.5" stop-color="#a86d45"/>
      <stop offset="1" stop-color="#d9a21e"/>
    </linearGradient>
    <marker id="head-red" viewBox="0 0 10 10" refX="5" refY="5" markerWidth="2.2" markerHeight="2.2" orient="auto">
      <path d="M0 0 L10 5 L0 10 Z" fill="var(--arrow-red)"/>
    </marker>
    <marker id="head-mist" viewBox="0 0 10 10" refX="5" refY="5" markerWidth="2.4" markerHeight="2.4" orient="auto">
      <path d="M0 0 L10 5 L0 10 Z" fill="var(--arrow-mist)"/>
    </marker>
    <marker id="head-teal" viewBox="0 0 10 10" refX="5" refY="5" markerWidth="2.6" markerHeight="2.6" orient="auto">
      <path d="M0 0 L10 5 L0 10 Z" fill="var(--teal)"/>
    </marker>
    <marker id="head-white" viewBox="0 0 10 10" refX="5" refY="5" markerWidth="3" markerHeight="3" orient="auto">
      <path d="M0 0 L10 5 L0 10 Z" fill="#e8f0fa"/>
    </marker>
    <path id="curve-left" d="M300 520 C 260 380, 290 250, 372 150"/>
    <path id="curve-right" d="M815 95 C 890 140, 940 200, 955 300"/>
    <path id="curve-discovery" d="M378 372 C 370 320, 382 275, 416 238"/>
  </defs>

  <rect class="paper" x="10" y="18" width="1120" height="664" fill="var(--paper)"/>

  <g class="cloud" fill="url(#cloud-fill)">
    <ellipse cx="580" cy="310" rx="380" ry="240"/>
    <ellipse cx="420" cy="120" rx="190" ry="90"/>
    <ellipse cx="720" cy="110" rx="230" ry="80"/>
    <ellipse cx="880" cy="230" rx="110" ry="170"/>
    <ellipse cx="260" cy="300" rx="90" ry="150"/>
    <ellipse cx="320" cy="470" rx="140" ry="90"/>
    <ellipse cx="820" cy="470" rx="160" ry="90"/>
    <ellipse cx="240" cy="420" rx="70" ry="70"/>
  </g>
  <g class="bubbles" fill="#3f6fb0" stroke="#b8d0ee" stroke-width="1">
    <circle cx="120" cy="455" r="45"/>
    <circle cx="58" cy="470" r="30"/>
    <circle cx="20" cy="478" r="15"/>
  </g>

  <ellipse class="orb" cx="575" cy="322" rx="222" ry="268" fill="var(--orb)" stroke="var(--orb-edge)" stroke-width="2"/>

  <text class="comfort-left"><textPath href="#curve-left">COMFORT</textPath></text>
  <text class="comfort-right"><textPath href="#curve-right">COMFOrt</textPath></text>

  <g class="title-label" transform="rotate(-4 170 100)">
    <path d="M42 40 L296 34 L290 150 L48 160 Z" fill="#fbfbfb"/>
    <text class="brand-name brand-faint" x="60" y="132" font-size="44">Tandemly</text>
    <text class="title-text" x="62" y="95">Principles of Action</text>
  </g>

  <path d="M488 420 C 400 440, 355 330, 390 268 C 405 240, 425 228, 445 218" fill="none" stroke="var(--arrow-red)" stroke-width="30" marker-end="url(#head-red)"/>
  <text class="discovery-text"><textPath href="#curve-discovery">Discovery</textPath></text>

  <path d="M690 212 C 790 215, 800 380, 708 422" fill="none" stroke="var(--arrow-mist)" stroke-width="20" marker-end="url(#head-mist)"/>

  <g class="eye-box">
    <rect x="466" y="138" width="224" height="152" fill="var(--ink)"/>
    <rect x="484" y="150" width="188" height="128" rx="10" fill="url(#eye-area-fill)" role="img" aria-label="Illustration of a golden eye seen from above"/>
    <text class="eye-small" x="500" y="164">information</text>
    <text class="eye-small" x="592" y="190">thought</text>
    <text class="eye-word" x="497" y="220">Birds</text>
    <text class="eye-word" x="566" y="224" font-style="italic">eye</text>
    <text class="eye-word" x="622" y="220">view</text>
    <text class="eye-caption" x="500" y="256">cognitive skill</text>
  </g>

  <g class="rapid-tag" transform="rotate(-8 780 312)">
    <rect x="708" y="282" width="146" height="60" fill="var(--ink)"/>
    <text class="tag-text" x="716" y="322">Rapid action</text>
  </g>

  <g class="agility-box">
    <rect x="484" y="330" width="200" height="136" fill="var(--white)"/>
    <text class="agility-word" x="546" y="378">Agility</text>
    <circle cx="572" cy="432" r="24" fill="var(--spiral)" opacity="0.85" role="img" aria-label="Red spiral motif"/>
  </g>

  <line x1="598" y1="468" x2="598" y2="536" stroke="var(--teal)" stroke-width="10" marker-end="url(#head-teal)"/>

  <g class="night-cloud" fill="var(--night-cloud)">
    <ellipse cx="610" cy="585" rx="165" ry="40"/>
    <ellipse cx="540" cy="568" rx="70" ry="28"/>
    <ellipse cx="680" cy="563" rx="80" ry="26"/>
  </g>
  <text class="complete-text" x="476" y="515">Complete</text>
  <text class="clarity-text" x="520" y="528">clarity</text>
  <text class="comfortable-text" x="490" y="604">Comfortable</text>

  <path d="M472 598 C 440 640, 380 630, 382 600" fill="none" stroke="#2b3a5a" stroke-width="8"/>
  <path d="M472 598 C 440 640, 380 630, 382 600" fill="none" stroke="#e8f0fa" stroke-width="4" marker-end="url(#head-white)"/>
  <g class="back-tag" transform="rotate(35 348 548)">
    <rect x="300" y="512" width="96" height="72" fill="var(--ink)"/>
    <g transform="rotate(180 348 548)">
      <text class="back-text" x="316" y="545">BACK</text>
      <text class="back-text" x="336" y="568" font-size="12">to</text>
    </g>
  </g>

  <g class="brand-corner">
    <rect x="932" y="566" width="168" height="58" fill="#f6f9fd"/>
    <text class="brand-name" x="946" y="605" font-size="30">Tandemly</text>
  </g>
</svg>
</body>
</html>
```